Portal Panel Medic need professional looking business card printed on plastic, Commericial, Industri

We are family owned and operated garage door company in Indianapolis, Indiana. We sale service and install dock equipment, doors, operators. We are looking to expand our commercial/ industrial division. We also service all residential doors and operators. We are looking for a business that stands out of the crowd. We are committed to have the best customer service in the industry.

Target Market(s)

National and local general contractors, National/ Corpate service accounts,

Industry/Entity Type

Business Service

Contact Information for Business Card

To be printed on plastic stock

Font styles to use
Sans Serif

Colors
ffffff
f04a50
ec1f27

Requirements
Must have
• Name, website,email, phone number, position.
Nice to have
• A standout professional design

```html
<!DOCTYPE html>
<html lang="en">
<head>
<meta charset="utf-8">
<title>Portal Panel Medic – Business Card</title>
<link rel="stylesheet" href="https://fonts.googleapis.com/css2?family=Open+Sans:wght@400&family=Tinos&display=swap">
<style>
  :root {
    --white: #ffffff;
    --red: #ec1f27;
    --red-soft: #f04a50;
    --charcoal: #222222;
    --mark-grey: #d6d6d6;
  }
  html, body {
    margin: 0;
    padding: 0;
    overflow: hidden;
    background: var(--white);
  }
  .card {
    position: relative;
    width: 1200px;
    height: 686px;
    background: var(--white);
    overflow: hidden;
    font-family: "Open Sans", sans-serif;
  }
  .brand {
    position: absolute;
    left: 0;
    top: 0;
    width: 1200px;
    height: 395px;
    display: flex;
    align-items: center;
    justify-content: center;
    gap: 26px;
  }
  .brand-dot {
    width: 84px;
    height: 84px;
    border-radius: 50%;
    background: var(--mark-grey);
    flex: none;
  }
  .brand-name {
    margin: 0;
    font-family: "Tinos", serif;
    font-weight: 400;
    font-size: 58px;
    line-height: 1;
    color: var(--red);
    letter-spacing: 1px;
    white-space: nowrap;
  }
  .info-band {
    position: absolute;
    left: 0;
    top: 395px;
    width: 1200px;
    height: 291px;
    background: var(--charcoal);
    color: var(--white);
  }
  .identity {
    position: absolute;
    right: 628px;
    top: 40px;
    text-align: right;
  }
  .person-name, .person-role {
    margin: 0;
    font-family: "Tinos", serif;
    font-weight: 400;
    font-size: 47px;
    line-height: 54px;
    letter-spacing: 1px;
  }
  .address {
    position: absolute;
    right: 635px;
    top: 169px;
    margin: 0;
    text-align: right;
    font-style: normal;
    font-size: 23px;
    line-height: 33px;
  }
  .contacts {
    position: absolute;
    left: 645px;
    top: 45px;
    margin: 0;
    padding: 0;
    list-style: none;
  }
  .contacts li {
    display: flex;
    align-items: center;
    height: 42px;
    margin-bottom: 10px;
    font-size: 24px;
  }
  .icon {
    width: 42px;
    height: 42px;
    border-radius: 50%;
    background: var(--white);
    display: flex;
    align-items: center;
    justify-content: center;
    margin-right: 30px;
    flex: none;
  }
  .icon svg { width: 24px; height: 24px; }
</style>
</head>
<body>
<div class="card">
  <div class="brand">
    <div class="brand-dot"></div>
    <h1 class="brand-name">Portal Panel Medic</h1>
  </div>

  <section class="info-band">
    <div class="identity">
      <p class="person-name">John Smith</p>
      <p class="person-role">Managing Director</p>
    </div>
    <address class="address">1234,Address GoesHere<br>Country,12345</address>

    <ul class="contacts">
      <li>
        <span class="icon">
          <svg viewBox="0 0 24 24"><path fill="#ec1f27" d="M6.6 10.8c1.4 2.8 3.8 5.1 6.6 6.6l2.2-2.2c.3-.3.7-.4 1-.2 1.1.4 2.3.6 3.6.6.6 0 1 .4 1 1V20c0 .6-.4 1-1 1C10.6 21 3 13.4 3 4c0-.6.4-1 1-1h3.5c.6 0 1 .4 1 1 0 1.3.2 2.5.6 3.6.1.3 0 .7-.2 1z"/></svg>
        </span>
        123-456-789
      </li>
      <li>
        <span class="icon">
          <svg viewBox="0 0 24 24"><path fill="#ec1f27" d="M6.6 10.8c1.4 2.8 3.8 5.1 6.6 6.6l2.2-2.2c.3-.3.7-.4 1-.2 1.1.4 2.3.6 3.6.6.6 0 1 .4 1 1V20c0 .6-.4 1-1 1C10.6 21 3 13.4 3 4c0-.6.4-1 1-1h3.5c.6 0 1 .4 1 1 0 1.3.2 2.5.6 3.6.1.3 0 .7-.2 1z"/></svg>
        </span>
        123-456-789
      </li>
      <li>
        <span class="icon">
          <svg viewBox="0 0 24 24"><rect x="2" y="5" width="20" height="14" rx="1" fill="#ec1f27"/><path d="M2.5 6l9.5 7 9.5-7" fill="none" stroke="#ffffff" stroke-width="1.6"/></svg>
        </span>
        info@youremail.com
      </li>
      <li>
        <span class="icon">
          <svg viewBox="0 0 24 24"><g fill="none" stroke="#ec1f27" stroke-width="1.8"><circle cx="12" cy="12" r="9"/><ellipse cx="12" cy="12" rx="4" ry="9"/><path d="M3 12h18M5 7h14M5 17h14"/></g></svg>
        </span>
        www.yourweb.com
      </li>
    </ul>
  </section>
</div>
</body>
</html>
```